Website improvements and Adding Functionalities at https://quorin.net/tamberly

1.Search functionality
2.Payment process functionality
3. Application configuration
4. Registration functionality activation
5. Chat functionality
6.Language switching functionality (Portuguese & French)
7.Bespoke interactive modules
8. Automated web scraping and data synchronisation mechanisms
9. News Page
10.Webinar facilities
11. Basic SEO optimisation
12. Speed and performance optimisation
13. Security configuration
14. Google Analytics integration
15. Cross-browser and mobile testing
16. Website deployment and launch support

Target Market(s)

My target markets are companies, investors, suppliers and professionals with an interest in the Mozambican oil and gas sector

Industry/Entity Type

Oil and Gas

Coding

Coded - Design and coding required

Number of Pages Required

1 page

Requirements
Must have
• Improve the existing page at https://quorin.net/tamberly and add the following features to it: 1. Search functionality 2. Payment process functionality 3. Application configuration 4. Activation of registration functionality 5. Chat functionality 6. Language switching functionality (Portuguese & French) 7. Bespoke interactive modules 8. Automated web scraping and data synchronisation mechanisms 9. News Page

```html
<!DOCTYPE html>
<html lang="en">
<head>
<meta charset="utf-8">
<title>Tamberly – Mozambique Oil &amp; Gas Intelligence</title>
<link rel="stylesheet" href="https://fonts.googleapis.com/css2?family=Inter:wght@400;500;600;700;800&display=swap">
<style>
:root{
  --orange:#f26a1b;
  --orange-deep:#e8501c;
  --navy:#1d1440;
  --navy-2:#2a1f5c;
  --heading:#2e2a6b;
  --ink:#333;
  --muted:#555;
  --sand:#f0eee9;
  --white:#fff;
}
*{box-sizing:border-box;margin:0;padding:0}
html,body{width:1200px;height:4950px;overflow:hidden}
body{font-family:"Inter",sans-serif;color:var(--ink);background:var(--white)}
.wrap{width:950px;margin:0 auto;position:relative}
.eyebrow{color:var(--orange-deep);font-weight:600;font-size:15px;letter-spacing:1.5px;text-align:center}
.eyebrow::before{content:"✦ "}
.section-title{color:var(--heading);font-weight:600;font-size:36px;text-align:center;margin-top:12px}
.btn{display:inline-block;font-size:15px;font-weight:500;padding:9px 16px;border-radius:3px;text-decoration:none}
.btn-orange{background:var(--orange);color:var(--white)}
.btn-ghost{border:1.5px solid var(--white);color:var(--white)}

/* header */
.site-header{height:129px;position:relative}
.brand{position:absolute;left:0;top:0;width:315px;height:129px;background:var(--white);display:flex;align-items:center;justify-content:center;gap:10px}
.brand-mark{width:22px;height:22px;background:var(--orange)}
.brand-name{font-weight:700;font-size:26px;color:var(--navy)}
.topbar{position:absolute;left:315px;right:0;top:0;height:50px;background:var(--navy);display:flex;align-items:center;padding:0 50px 0 70px;color:var(--white);font-size:19px}
.topbar .mail{display:flex;align-items:center;gap:8px}
.topbar .tools{margin-left:auto;display:flex;align-items:center;gap:16px}
.lang{background:var(--orange);border-radius:3px;padding:3px 10px;font-size:16px;font-weight:600}
.register{background:var(--white);color:var(--orange-deep);font-size:16px;font-weight:600;padding:4px 18px;border-radius:3px}
.mainnav{position:absolute;left:315px;right:0;top:50px;height:79px;background:var(--orange);display:flex;align-items:center;gap:22px;padding-left:40px}
.mainnav a{color:var(--white);font-size:16px;text-decoration:none}

/* hero */
.hero{height:621px;position:relative;background:linear-gradient(90deg,#2b2530 0%,#4a3a34 45%,#8a6a4a 75%,#b07a4a 100%)}
.hero .photo{position:absolute;inset:0;background:linear-gradient(180deg,rgba(30,25,40,.2),rgba(20,20,30,.55))}
.hero-copy{position:absolute;left:125px;top:118px;width:470px;color:var(--white)}
.hero-copy h1{font-size:50px;font-weight:700;line-height:58px}
.hero-copy p{font-size:14px;line-height:21px;margin:24px 0 24px}

/* about */
.about{height:740px;position:relative}
.about .frame-a{position:absolute;left:95px;top:130px;width:153px;height:163px;border:1.5px solid var(--orange);border-radius:14px}
.about .frame-b{position:absolute;left:470px;top:484px;width:153px;height:163px;border:1.5px solid var(--orange);border-radius:14px}
.about .photo{position:absolute;left:125px;top:154px;width:465px;height:465px;border-radius:22px;border:6px solid var(--white);box-shadow:0 0 0 2px #ccc,0 10px 24px rgba(0,0,0,.18);background:linear-gradient(180deg,#2b3350 0%,#5a4a60 35%,#c08040 70%,#3a2a30 100%)}
.about-copy{position:absolute;left:660px;top:214px;width:420px}
.about-copy .eyebrow{text-align:left}
.about-copy h2{color:var(--heading);font-size:35px;font-weight:600;margin:10px 0 16px}
.about-copy p{font-size:14px;line-height:22px;margin-bottom:16px;color:var(--ink)}

/* capabilities */
.capabilities{height:823px;background:var(--sand);padding-top:100px}
.cap-grid{display:grid;grid-template-columns:repeat(3,306px);gap:16px;margin-top:40px}
.cap-card{height:227px;border-radius:12px;background:linear-gradient(180deg,#2d1d6a 0%,var(--navy) 100%);color:var(--white);text-align:center;padding:16px 30px 0}
.cap-card svg{width:72px;height:72px}
.cap-card h3{font-size:19px;font-weight:600;line-height:24px;margin-top:8px}
.cap-card p{font-size:14px;line-height:21px;color:#e0dcef;margin-top:12px}
.cap-more{text-align:center;margin-top:48px}

/* process */
.process{height:583px;background:linear-gradient(180deg,#2a2158 0%,#241b4d 60%,#2a2158 100%);padding-top:90px;color:var(--white)}
.process .eyebrow{color:var(--orange)}
.process .section-title{color:var(--white)}
.steps{display:flex;justify-content:space-between;margin-top:44px;padding:0 10px}
.step{width:160px;text-align:center}
.diamond{width:96px;height:96px;margin:12px auto 0;border:2.5px solid var(--orange);border-radius:10px;transform:rotate(45deg);display:flex;align-items:center;justify-content:center}
.diamond svg{transform:rotate(-45deg);width:60px;height:60px}
.step .num{width:48px;height:48px;margin:40px auto 0;border-radius:50%;background:var(--orange);font-weight:700;font-size:20px;line-height:48px}
.step h3{font-size:20px;font-weight:700;line-height:25px;margin-top:24px}

/* advantages */
.advantages{height:585px;background:var(--sand);padding-top:116px}
.adv-grid{display:grid;grid-template-columns:repeat(3,306px);gap:16px;margin-top:64px}
.adv-card{height:241px;background:var(--white);border-radius:12px;box-shadow:0 3px 10px rgba(0,0,0,.08);text-align:center;padding:16px 24px 0}
.adv-icon{width:96px;height:76px;margin:0 auto;border-radius:6px;background:var(--navy);display:flex;align-items:center;justify-content:center}
.adv-icon.teal{background:#1f4a4a}
.adv-card h3{color:var(--heading);font-size:19px;font-weight:700;line-height:24px;margin-top:10px}
.adv-card p{font-size:14px;line-height:21px;color:var(--muted);margin-top:10px}

/* audience */
.audience{height:640px;padding-top:112px}
.aud-grid{display:grid;grid-template-columns:repeat(3,306px);gap:16px;margin-top:58px}
.aud-card{height:300px;border-radius:12px;box-shadow:0 3px 10px rgba(0,0,0,.1);overflow:hidden;background:var(--white)}
.aud-photo{height:220px;position:relative;display:flex;align-items:flex-end;justify-content:center}
.aud-photo span{position:relative;width:100%;text-align:center;padding:8px 0;background:linear-gradient(0deg,rgba(20,20,40,.7),transparent);color:var(--white);font-weight:700;font-size:19px}
.ph-investor{background:linear-gradient(180deg,#dfe3e6,#9aa3ab)}
.ph-epc{background:linear-gradient(180deg,#a07048,#5a3a28)}
.ph-gov{background:linear-gradient(180deg,#d6e6f2,#c9b48c)}
.aud-card p{font-size:14px;line-height:21px;color:var(--muted);text-align:center;padding:12px 28px 0}

/* cta */
.cta{height:481px;background:linear-gradient(180deg,#d9e6ef 0%,#bcd0de 100%);padding-top:92px}
.cta-card{width:950px;height:299px;margin:0 auto;border-radius:18px;background:linear-gradient(90deg,#f5861f 0%,var(--orange-deep) 100%);text-align:center;color:var(--white);padding-top:64px}
.cta-card h2{font-size:36px;font-weight:700;line-height:42px}
.cta-card p{font-size:15px;line-height:22px;margin:24px auto 18px;width:700px}
.btn-dark{background:var(--navy);color:var(--white);margin-right:10px}

/* footer */
.site-footer{height:348px;background:var(--navy);color:var(--white);position:relative}
.foot-brand{position:absolute;left:125px;top:88px;width:170px}
.foot-brand .brand-name{color:var(--white);font-size:22px;display:flex;align-items:center;gap:8px}
.foot-brand p{font-size:11px;line-height:15px;margin-top:12px;color:#d8d4e8}
.foot-col{position:absolute;top:78px}
.foot-col h4{color:var(--orange);font-size:16px;font-weight:600;letter-spacing:1px;margin-bottom:20px}
.foot-col li{list-style:none;font-size:14px;margin-bottom:24px}
.foot-col p{font-size:14px;line-height:21px;width:230px}
.subscribe{display:flex;margin-top:12px;width:230px;height:36px}
.subscribe span{flex:1;border:1px solid #8a84a8;border-radius:3px 0 0 3px;font-size:12px;color:#8a84a8;padding:10px 10px}
.subscribe b{width:46px;background:var(--orange);border-radius:0 3px 3px 0;display:flex;align-items:center;justify-content:center}
.foot-bottom{position:absolute;left:125px;right:125px;top:300px;border-top:1px solid #3f3670;padding-top:20px;font-size:14px;display:flex;align-items:center}
.socials{margin-left:auto;display:flex;gap:34px}
.socials i{width:28px;height:28px;border-radius:50%;background:var(--white);display:block}
</style>
</head>
<body>

<header class="site-header">
  <div class="brand"><span class="brand-mark"></span><span class="brand-name">Tamberly</span></div>
  <div class="topbar">
    <span class="mail"><svg width="20" height="16" viewBox="0 0 20 16"><rect x="1" y="1" width="18" height="14" rx="2" fill="#fff"/><path d="M2 3l8 6 8-6" stroke="#1d1440" stroke-width="1.6" fill="none"/></svg>contacto@tamberly.net</span>
    <span class="tools">
      <svg width="20" height="20" viewBox="0 0 20 20"><circle cx="8" cy="8" r="6" stroke="#fff" stroke-width="2" fill="none"/><path d="M13 13l5 5" stroke="#fff" stroke-width="2"/></svg>
      <span class="lang">EN ▾</span>
      <span class="register">Register</span>
    </span>
  </div>
  <nav class="mainnav">
    <a href="#">Home</a><a href="#">Industry Insights</a><a href="#">Oil &amp; Gas Opportunities</a><a href="#">Supplier &amp; Company Network</a><a href="#">Legal Framework</a>
  </nav>
</header>

<section class="hero">
  <div class="photo" role="img" aria-label="Engineers in hard hats looking out over an offshore oil platform at sunset"></div>
  <div class="hero-copy">
    <h1>Access Mozambique’s Oil &amp; Gas Industry Intelligence in One Platform</h1>
    <p>Tamberly is a modern online connection and consulting platform designed to facilitate access to the Mozambican Oil and Gas industry through premium industry insights, supplier information, tenders, legal frameworks, and strategic project data.</p>
    <a class="btn btn-orange" href="#">Explore Platform</a>
    <a class="btn btn-ghost" href="#" style="margin-left:6px">Become a Member</a>
  </div>
</section>

<section class="about">
  <div class="frame-a"></div>
  <div class="frame-b"></div>
  <div class="photo" role="img" aria-label="Refinery lit up at dusk beside the water"></div>
  <div class="about-copy">
    <div class="eyebrow">ABOUT</div>
    <h2>What is Tamberly?</h2>
    <p>Tamberly is a unique online platform built to connect businesses, investors, suppliers, and professionals with valuable information about the Mozambican Oil &amp; Gas industry.</p>
    <p>Through a secure digital paywall system, users gain access to organized, up-to-date, and carefully selected industry information that supports better decision-making, market understanding, and business opportunities within Mozambique's growing hydrocarbons industry.</p>
    <a class="btn btn-orange" href="#">Explore Services</a>
  </div>
</section>

<section class="capabilities">
  <div class="wrap">
    <div class="eyebrow">CAPABILITIES</div>
    <h2 class="section-title">Everything You Need in One Place</h2>
    <div class="cap-grid">
      <div class="cap-card">
        <svg viewBox="0 0 72 72" fill="none" stroke="#fff" stroke-width="2"><path d="M36 10l-10 52h20z"/><path d="M30 30h12M28 42h16"/><path d="M14 20c-4 6-4 10 0 12 4-2 4-6 0-12zM58 20c-4 6-4 10 0 12 4-2 4-6 0-12z"/></svg>
        <h3>Hydrocarbon Industry Information</h3>
        <p>General information and insights about Mozambique's oil and gas sector.</p>
      </div>
      <div class="cap-card">
        <svg viewBox="0 0 72 72" fill="none" stroke="#fff" stroke-width="2"><path d="M20 62V24l8-12M28 12h20l-6 14H20"/><path d="M40 26v36M12 62h48"/><rect x="46" y="44" width="10" height="18"/></svg>
        <h3>Main Gas Projects</h3>
        <p>Details about major gas and energy projects operating in Mozambique.</p>
      </div>
      <div class="cap-card">
        <svg viewBox="0 0 72 72" fill="none" stroke="#fff" stroke-width="2"><path d="M12 32l24-18 24 18v28H12z"/><rect x="24" y="36" width="24" height="16" rx="2"/><circle cx="30" cy="54" r="3"/><circle cx="42" cy="54" r="3"/></svg>
        <h3>Supplier &amp; Company Database</h3>
        <p>Mozambican companies capable of meeting Local &amp; supply requirements.</p>
      </div>
      <div class="cap-card">
        <svg viewBox="0 0 72 72" fill="none" stroke="#fff" stroke-width="2"><circle cx="24" cy="28" r="10"/><circle cx="48" cy="22" r="10"/><circle cx="44" cy="50" r="10"/><path d="M33 25l6-2M30 36l8 8"/></svg>
        <h3>Industry Contacts</h3>
        <p>Key contacts from NOCs, Operators, EPCs, and Second-Tier Suppliers.</p>
      </div>
      <div class="cap-card">
        <svg viewBox="0 0 72 72" fill="none" stroke="#fff" stroke-width="2"><path d="M18 10h26l10 10v40H18z"/><path d="M44 10v10h10M24 28h18M24 36h14M24 44h10"/><circle cx="46" cy="48" r="8"/></svg>
        <h3>Tender Opportunities</h3>
        <p>Short, medium, and long-term tenders within the industry.</p>
      </div>
      <div class="cap-card">
        <svg viewBox="0 0 72 72" fill="none" stroke="#fff" stroke-width="2"><path d="M10 30l14-10 12 6 12-6 14 10"/><path d="M24 40l10 10 16-16"/><circle cx="36" cy="14" r="5"/></svg>
        <h3>Ownership &amp; Access</h3>
        <p>Information related to hydrocarbon reserves and sector participation.</p>
      </div>
    </div>
    <div class="cap-more"><a class="btn btn-orange" href="#">Explore More</a></div>
  </div>
</section>

<section class="process">
  <div class="wrap">
    <div class="eyebrow">PROCESS</div>
    <h2 class="section-title">How the Platform Works</h2>
    <div class="steps">
      <div class="step"><div class="diamond"><svg viewBox="0 0 60 60" fill="none" stroke="#fff" stroke-width="2"><rect x="10" y="14" width="40" height="32" rx="3"/><path d="M10 22h40"/><circle cx="30" cy="32" r="5"/></svg></div><div class="num">1</div><h3>Register Securely</h3></div>
      <div class="step"><div class="diamond"><svg viewBox="0 0 60 60" fill="none" stroke="#fff" stroke-width="2"><rect x="14" y="10" width="32" height="26" rx="3"/><path d="M26 30v18M26 40h12v10H22"/></svg></div><div class="num">2</div><h3>Subscribe Securely</h3></div>
      <div class="step"><div class="diamond"><svg viewBox="0 0 60 60" fill="none" stroke="#fff" stroke-width="2"><circle cx="36" cy="22" r="8"/><path d="M36 18v8M14 46h14v-8h-8"/><circle cx="20" cy="46" r="4"/></svg></div><div class="num">3</div><h3>Unlock Premium Access</h3></div>
      <div class="step"><div class="diamond"><svg viewBox="0 0 60 60" fill="none" stroke="#fff" stroke-width="2"><path d="M12 48h36M16 48V36h6v12M27 48V30h6v18M38 48V24h6v24M14 28l14-10 8 4 12-10"/></svg></div><div class="num">4</div><h3>Grow with Confidence</h3></div>
      <div class="step"><div class="diamond"><svg viewBox="0 0 60 60" fill="none" stroke="#fff" stroke-width="2"><circle cx="30" cy="30" r="18"/><path d="M38 22l-5 11-11 5 5-11z"/></svg></div><div class="num">5</div><h3>Explore the Platform</h3></div>
    </div>
  </div>
</section>

<section class="advantages">
  <div class="wrap">
    <div class="eyebrow">ADVANTAGES</div>
    <h2 class="section-title">Why Tamberly Is Unique</h2>
    <div class="adv-grid">
      <div class="adv-card">
        <div class="adv-icon"><svg width="54" height="54" viewBox="0 0 54 54" fill="none" stroke="#fff" stroke-width="2"><circle cx="27" cy="27" r="8"/><rect x="10" y="10" width="34" height="34" rx="4"/></svg></div>
        <h3>Up-to-date Industry Intelligence</h3>
        <p>Premium reports updated about the latest developments in Mozambique's Oil &amp; Gas sector.</p>
      </div>
      <div class="adv-card">
        <div class="adv-icon"><svg width="54" height="54" viewBox="0 0 54 54" fill="none" stroke="#fff" stroke-width="2"><path d="M27 8l14 6v12c0 10-6 16-14 20-8-4-14-10-14-20V14z"/><path d="M20 27l5 5 10-10"/></svg></div>
        <h3>High-Quality Curated Information</h3>
        <p>Access carefully selected and synthesized information tailored to industry needs.</p>
      </div>
      <div class="adv-card">
        <div class="adv-icon teal"><svg width="54" height="54" viewBox="0 0 54 54" fill="none" stroke="#fff" stroke-width="2"><circle cx="24" cy="26" r="16"/><path d="M24 16v10l7 4"/><circle cx="40" cy="40" r="7"/><path d="M36 40l3 3 5-6"/></svg></div>
        <h3>Time-Saving Access</h3>
        <p>Find everything you need searching through organized content and a reliable system in one platform.</p>
      </div>
    </div>
  </div>
</section>

<section class="audience">
  <div class="wrap">
    <div class="eyebrow">AUDIENCE</div>
    <h2 class="section-title">Who Is It For?</h2>
    <div class="aud-grid">
      <div class="aud-card"><div class="aud-photo ph-investor" role="img" aria-label="Investor reviewing documents at a desk"><span>Investors</span></div><p>Evaluate opportunities with reliable market intelligence.</p></div>
      <div class="aud-card"><div class="aud-photo ph-epc" role="img" aria-label="Contractor in hard hat and safety vest on a site"><span>EPC Contractors</span></div><p>Connect with qualified local businesses.</p></div>
      <div class="aud-card"><div class="aud-photo ph-gov" role="img" aria-label="Government building with landscaped grounds"><span>Government Agencies</span></div><p>Access industry information that supports planning and development.</p></div>
    </div>
  </div>
</section>

<section class="cta" role="img" aria-label="Faded industrial plant backdrop">
  <div class="cta-card">
    <h2>Start Exploring Mozambique's Oil &amp; Gas<br>Opportunities</h2>
    <p>Register today to access premium industry information, supplier networks, tenders, and strategic market insights through Tamberly.</p>
    <a class="btn btn-dark" href="#">Request Demo</a><a class="btn btn-ghost" href="#">Contact Us</a>
  </div>
</section>

<footer class="site-footer">
  <div class="foot-brand">
    <div class="brand-name"><span class="brand-mark" style="width:18px;height:18px"></span>Tamberly</div>
    <p>Mozambique Oil &amp; Gas connection &amp; consulting platform.</p>
  </div>
  <div class="foot-col" style="left:350px"><h4>PLATFORM</h4><ul><li>Industry Insights</li><li>Oil &amp; Gas Opportunities</li><li>Supplier &amp; Company Network</li><li>News</li></ul></div>
  <div class="foot-col" style="left:608px"><h4>COMPANY</h4><ul><li>What is Tamberly?</li><li>Bespoke Interactive Modules</li><li>Who Is It For?</li><li>Contact Us</li></ul></div>
  <div class="foot-col" style="left:847px"><h4>SUBSCRIBE</h4><p>Get weekly industry intelligence in your inbox.</p>
    <div class="subscribe"><span>you@company.com</span><b><svg width="20" height="14" viewBox="0 0 20 14"><path d="M1 7h17M12 1l6 6-6 6" stroke="#fff" stroke-width="2" fill="none"/></svg></b></div>
  </div>
  <div class="foot-bottom">© 2026 Tamberly. All rights reserved.<span class="socials"><i></i><i></i><i></i><i></i></span></div>
</footer>

</body>
</html>
```